Business Cards for Bramblewood Coatings Pty Ltd

Hi every one i need a design for my buisness cards. I Want my logo in it and the name of the company needs to stand out Bramblewood Coatings Pty Ltd. I want the background of the buisness cards black and i want the font to stand out in either a white or a silver stylish text. I want the design to be simple but original not to in your face if you know what i mean. I want on the back of the buisness cards to have the services that my buisness offers.
• Interior/Exterior
• Residential/Commercial
• Special effects/Texture Coatings
• Water Damage Repair
• Fully qualified
• Pensioner Discount
• 10 Year guarantee
• Fully Insured
• Obligation free quotes
full internal repaints include a proffesionla cleaning service
I want the services on the back to be layed out in an originall way not just dot points. If possible could my logo take up the whole back ground of the back but the text with the services be kind of like transparent so u cvan still see the logo i dont know if its possible it woiuld just look cool if possible. When i pick a design ill give my contact details to the designer to add to the design at the end. Any questions please just ask! Ill upload my logo.
Conatcs will include office phone: Mobile: E-mail - dean@bramblewoodcoatings.com.au, Ill also have a Postal address which is a PO Box and my website is www.bramblewoodcoatings.com.au

```html
<!DOCTYPE html>
<html lang="en">
<head>
<meta charset="utf-8">
<title>Bramblewood Coatings Pty Ltd – Business Cards</title>
<link rel="stylesheet" href="https://fonts.googleapis.com/css2?family=Arimo:wght@400;700&family=Archivo+Narrow:wght@400;600&family=Courier+Prime:ital,wght@0,400;0,700;1,400&display=swap">
<style>
  :root {
    --backdrop: #2b2925;
    --card: #000000;
    --silver: #cfcfcf;
    --silver-dark: #8c8c8c;
    --white: #ffffff;
    --mist: #9a9a9a;
    --ghost: rgba(255, 255, 255, 0.14);
  }
  * { box-sizing: border-box; margin: 0; padding: 0; }
  html, body {
    width: 1200px; height: 857px; overflow: hidden;
    background: var(--backdrop);
  }
  .stage { position: relative; width: 1200px; height: 857px; }

  .card {
    position: absolute;
    background: var(--card);
    overflow: hidden;
  }

  /* Front */
  .card-front { left: 60px; top: 93px; width: 600px; height: 343px; }
  .brand-mark {
    position: absolute; left: 50%; top: 18px;
    width: 184px; height: 184px; margin-left: -92px;
    background: var(--silver-dark);
    border-radius: 10px;
  }
  .brand-name {
    position: absolute; left: 0; right: 0; top: 222px;
    text-align: center;
    font-family: "Arimo", Arial, sans-serif;
    font-weight: 700;
    color: var(--silver);
    line-height: 1.3;
  }
  .brand-name .line-main { display: block; font-size: 31px; letter-spacing: 0.5px; }
  .brand-name .line-sub { display: block; font-size: 26px; margin-top: 4px; }

  /* Back */
  .card-back { left: 560px; top: 440px; width: 580px; height: 340px; }
  .back-frame {
    position: absolute; left: 14px; top: 30px; right: 14px; bottom: 30px;
    border: 1px solid var(--mist);
  }
  .ghost-name {
    position: absolute; left: 0; right: 0; top: 124px;
    text-align: center;
    font-family: "Arimo", Arial, sans-serif; font-weight: 700;
    font-size: 70px; color: var(--ghost);
  }
  .t { position: absolute; white-space: nowrap; color: var(--white); transform-origin: left top; line-height: 1.1; }
  .contact { font-family: "Courier Prime", "Courier New", monospace; font-size: 13px; }
  .narrow { font-family: "Archivo Narrow", "Arial Narrow", sans-serif; }
  .script { font-family: "Courier Prime", "Courier New", monospace; font-style: italic; }
  .mono-bold { font-family: "Courier Prime", "Courier New", monospace; font-weight: 700; }

  .mobile { left: 22px; top: 9px; }
  .email { left: 205px; top: 9px; font-size: 12.5px; }
  .postbox { left: 22px; top: 316px; }
  .website { right: 22px; top: 316px; }

  .quotes { left: 318px; top: 44px; font-size: 15px; transform: rotate(-4deg); }
  .qualified { left: 524px; top: 262px; font-size: 27px; font-weight: 600; transform: rotate(-90deg); }
  .commercial { left: 490px; top: 218px; font-size: 17px; font-style: italic; transform: rotate(-90deg); }
  .special { left: 420px; top: 190px; font-size: 20px; transform: rotate(-72deg); }
  .insured { left: 52px; top: 100px; font-size: 34px; font-weight: 600; transform: rotate(-10deg); }
  .water { left: 70px; top: 184px; font-size: 23px; color: var(--mist); transform: rotate(-10deg); }
  .interior { left: 332px; top: 148px; font-size: 16px; transform: rotate(-8deg); }
  .residential { left: 288px; top: 200px; font-size: 13px; transform: rotate(-8deg); }
  .texture { left: 345px; top: 262px; font-size: 25px; color: var(--mist); transform: rotate(-10deg); }
  .exterior { left: 100px; top: 282px; font-size: 20px; transform: rotate(-65deg); }
  .guarantee { left: 150px; top: 278px; font-size: 18px; transform: rotate(-6deg); }
  .pensioner { left: 26px; top: 296px; font-size: 17px; transform: rotate(-90deg); }
</style>
</head>
<body>
<main class="stage">
  <section class="card card-front" aria-label="Front of business card">
    <div class="brand-mark"></div>
    <h1 class="brand-name">
      <span class="line-main">BRAMBLEWOOD COATINGS</span>
      <span class="line-sub">PTY LTD</span>
    </h1>
  </section>

  <section class="card card-back" aria-label="Back of business card">
    <div class="back-frame"></div>
    <div class="ghost-name" aria-hidden="true">Bramblewood</div>

    <span class="t contact mobile">mobile:0412 345 678</span>
    <span class="t contact email">e-mail:dean@bramblewoodcoatings.com.au</span>

    <span class="t script quotes">Obligation free quotes</span>
    <span class="t narrow qualified">fully qualified</span>
    <span class="t narrow commercial">commercial</span>
    <span class="t narrow special">special effect</span>
    <span class="t narrow insured">Fully Insured</span>
    <span class="t narrow water">water damage repair</span>
    <span class="t script interior">interior</span>
    <span class="t script residential">residential</span>
    <span class="t narrow texture">texture coatings</span>
    <span class="t narrow exterior">exterior</span>
    <span class="t mono-bold guarantee">10 Year guarantee</span>
    <span class="t mono-bold pensioner">Pensioner Discount</span>

    <span class="t contact postbox">Po Box:4471</span>
    <span class="t contact website">www.bramblewoodcoatings.com.au</span>
  </section>
</main>
</body>
</html>
```